既存の看板(居酒屋)がついているのでお昼ラーメンをやっているのがとても分かりづらく新規の集客に困っています。

のぼりをみてお店に入ってもらえるようなデザインをよろしくお願いします。
(HP、インスタを見て頂き、デザインやキャッチコピーはプロの方にお任せ致します)
好き勝手デザインしてくださいm(__)m

■お店の詳細
●HP
https://www.hanamoriya.net/korokibe/
●インスタ
https://www.instagram.com/korokibe.menyasan/
現在の外観A看板、のぼりの写真張っておきます。
素材でつかう写真も添付しておきます

※同時にA看板のデザインも募集しているのでよろしければそちらもご参加ください。
のぼりのサイズです。
A看板のデザインも大募集!
https://www.sakuhinbo.jp/work/detail/7182950
期間を延ばしてほしいとの要望がありましたので二日だけ延長致します。
よろしくお願いします。

バランスが良くみやすかったです。

たくさんのご提案ありがとうございました。

```html
<!DOCTYPE html>
<html lang="ja">
<head>
<meta charset="utf-8">
<title>雲呑麺 ゆらめき のぼり</title>
<link rel="stylesheet" href="https://fonts.googleapis.com/css2?family=Yuji+Boku&family=Yuji+Syuku&family=Shippori+Mincho:wght@500;700&display=swap">
<style>
  :root {
    --paper: #ffffff;
    --taupe: #a6978a;
    --taupe-light: #c9beb3;
    --umber: #5b4738;
    --umber-deep: #2f221a;
    --ink: #1c1612;
    --seal-red: #b8232a;
    --broth: #d9c089;
    --gold: #d4a93c;
    --gold-light: #f0d27a;
  }
  html, body {
    margin: 0;
    padding: 0;
    width: 1200px;
    height: 3596px;
    overflow: hidden;
    background: var(--paper);
  }
  .banner {
    position: relative;
    width: 1200px;
    height: 3596px;
    overflow: hidden;
    background: linear-gradient(180deg, var(--taupe-light) 0%, var(--taupe) 55%, var(--umber) 72%, var(--umber-deep) 100%);
  }
  .backdrop, .confetti {
    position: absolute;
    left: 0;
    top: 0;
  }
  .title { margin: 0; font-weight: 400; }
  .title-char {
    position: absolute;
    font-family: "Yuji Boku", "Yuji Syuku", serif;
    color: var(--ink);
    line-height: 1;
    z-index: 2;
  }
  .title-un  { left: 60px;  top: -30px;  font-size: 900px; }
  .title-don { left: 40px;  top: 840px;  font-size: 800px; }
  .title-men { left: 430px; top: 1710px; font-size: 820px; }

  .shop-name {
    position: absolute;
    left: 930px;
    top: 660px;
    margin: 0;
    writing-mode: vertical-rl;
    font-family: "Yuji Syuku", serif;
    font-size: 140px;
    letter-spacing: 4px;
    color: var(--ink);
    line-height: 1;
    z-index: 3;
  }
  .shop-tagline {
    position: absolute;
    left: 1070px;
    top: 740px;
    margin: 0;
    writing-mode: vertical-rl;
    font-family: "Shippori Mincho", serif;
    font-size: 38px;
    color: var(--ink);
    line-height: 1;
    z-index: 3;
  }
  .shop-seal {
    position: absolute;
    width: 84px;
    height: 84px;
    left: 770px;
    top: 1250px;
    border: 5px solid var(--seal-red);
    border-radius: 8px;
    box-sizing: border-box;
    z-index: 3;
  }
  .reading {
    position: absolute;
    left: 340px;
    top: 1880px;
    margin: 0;
    writing-mode: vertical-rl;
    font-family: "Shippori Mincho", serif;
    font-weight: 700;
    font-size: 54px;
    letter-spacing: 4px;
    color: var(--ink);
    line-height: 1;
    z-index: 3;
  }
  .confetti { z-index: 4; }
  .dish-photo {
    position: absolute;
    left: 0;
    top: 2600px;
    width: 1200px;
    height: 996px;
    z-index: 1;
  }
</style>
</head>
<body>
  <main class="banner">
    <svg class="backdrop" viewBox="0 0 1200 3596" width="1200" height="3596" aria-hidden="true">
      <rect class="pattern-band-top" x="0" y="0" width="1200" height="760" fill="var(--taupe)" role="img" aria-label="和柄の波模様"/>
      <rect class="pattern-band-left" x="0" y="1700" width="1200" height="1000" fill="var(--umber)" role="img" aria-label="和柄の波模様"/>
      <ellipse class="light-oval" cx="820" cy="1380" rx="820" ry="1420" fill="var(--paper)"/>
      <rect class="light-top" x="560" y="0" width="640" height="520" fill="var(--paper)"/>
    </svg>

    <h1 class="title">
      <span class="title-char title-un">雲</span>
      <span class="title-char title-don">呑</span>
      <span class="title-char title-men">麺</span>
    </h1>

    <p class="shop-name">ゆらめき</p>
    <p class="shop-tagline">雲呑麺のお店</p>
    <span class="shop-seal" aria-hidden="true"></span>
    <p class="reading">ワンタンメン</p>

    <svg class="confetti" viewBox="0 0 1200 3596" width="1200" height="3596" aria-hidden="true">
      <g fill="var(--gold)">
        <rect x="620" y="140" width="26" height="16" transform="rotate(25 633 148)"/>
        <rect x="880" y="470" width="22" height="14" transform="rotate(-30 891 477)"/>
        <rect x="560" y="560" width="30" height="18" transform="rotate(40 575 569)"/>
        <rect x="320" y="720" width="24" height="15" transform="rotate(-15 332 727)"/>
        <rect x="230" y="1140" width="28" height="17" transform="rotate(35 244 1148)"/>
        <rect x="40" y="1340" width="22" height="14" transform="rotate(-40 51 1347)"/>
        <rect x="660" y="1440" width="26" height="16" transform="rotate(20 673 1448)"/>
        <rect x="1020" y="1620" width="24" height="15" transform="rotate(-25 1032 1627)"/>
        <rect x="900" y="2230" width="30" height="18" transform="rotate(30 915 2239)"/>
        <rect x="1100" y="2420" width="22" height="14" transform="rotate(-35 1111 2427)"/>
        <rect x="560" y="2480" width="26" height="16" transform="rotate(15 573 2488)"/>
      </g>
      <g fill="var(--gold-light)">
        <rect x="760" y="300" width="18" height="12" transform="rotate(-20 769 306)"/>
        <rect x="460" y="620" width="20" height="12" transform="rotate(50 470 626)"/>
        <rect x="700" y="1000" width="18" height="11" transform="rotate(-45 709 1005)"/>
        <rect x="120" y="1600" width="20" height="12" transform="rotate(30 130 1606)"/>
        <rect x="1120" y="1900" width="18" height="11" transform="rotate(-15 1129 1905)"/>
        <rect x="820" y="2540" width="20" height="12" transform="rotate(40 830 2546)"/>
        <rect x="1000" y="2560" width="18" height="11" transform="rotate(-30 1009 2565)"/>
      </g>
    </svg>

    <svg class="dish-photo" viewBox="0 0 1200 996" width="1200" height="996" role="img" aria-label="チャーシュー、雲呑、メンマ、海苔、三つ葉をのせた澄んだスープの雲呑麺の写真">
      <defs>
        <radialGradient id="bowl-tone" cx="50%" cy="40%" r="70%">
          <stop offset="0%" stop-color="var(--broth)"/>
          <stop offset="55%" stop-color="#efe8dc"/>
          <stop offset="100%" stop-color="var(--umber-deep)"/>
        </radialGradient>
      </defs>
      <rect width="1200" height="996" fill="url(#bowl-tone)"/>
    </svg>
  </main>
</body>
</html>
```